Hope KLN Disease (Non-Profit) Tri-Fold Brochure Design

We have put together the content for a brochure that we will distribute to doctors, researchers and patients about our non-profit. We would like the design of the brochure to look more professional and have nice aesthetics. It needs to incorporate all of the content in the attached Word file. We will have printed once we have a finished design.

Target Market(s)

Medical

Industry/Entity Type

Non Profit

Font styles to use
Serif
Sans Serif

Colors
33a6d7

Requirements
Must have
• Must include all content provided. Professional.
Nice to have
• Colors

```html
<!DOCTYPE html>
<html lang="en">
<head>
<meta charset="utf-8">
<title>Hope KLN Disease – Tri-Fold Brochure</title>
<link href="https://fonts.googleapis.com/css2?family=Montserrat:wght@500;600;700&family=Open+Sans:wght@400;600;700&family=Quicksand:wght@500;600&display=swap" rel="stylesheet">
<style>
  :root{
    --teal:#1fa7b8;
    --teal-bright:#33a6d7;
    --teal-dark:#0e5f6d;
    --cyan-soft:#d6f6f9;
    --ink:#2b2f33;
    --ink-soft:#4a5157;
    --paper:#ffffff;
    --stage:#e8ebed;
  }
  *{box-sizing:border-box;margin:0;padding:0}
  html,body{width:1200px;height:1200px;overflow:hidden;background:var(--stage)}
  body{font-family:"Open Sans",Arial,sans-serif;color:var(--ink);position:relative}
  .sheet{position:absolute;left:40px;width:1120px;height:560px;display:grid;grid-template-columns:repeat(3,1fr);background:var(--paper);box-shadow:0 2px 10px rgba(0,0,0,.12)}
  .sheet--outside{top:20px}
  .sheet--inside{top:620px}
  .panel{position:relative;padding:22px 24px 58px;border-right:1px solid #eef1f2;overflow:hidden}
  .panel:last-child{border-right:none}
  .panel-foot{position:absolute;left:0;right:0;bottom:0;height:38px;background:var(--teal-dark);border-top:5px solid var(--teal);display:flex;align-items:center;justify-content:center;color:#fff;font-family:"Montserrat",sans-serif;font-weight:600;font-size:11px;letter-spacing:3px}
  h2.section-title{font-family:"Montserrat",sans-serif;font-weight:700;font-size:13px;color:var(--ink);letter-spacing:.5px;margin-bottom:5px}
  h3.sub-title{font-family:"Open Sans",sans-serif;font-weight:700;font-size:9.5px;margin-top:6px}
  p,li{font-size:9.2px;line-height:1.38;color:var(--ink-soft)}
  .callout{background:var(--cyan-soft);padding:12px 14px;margin-bottom:14px}
  .callout p+p{margin-top:8px}
  .bullets{list-style:none;margin-top:6px}
  .bullets li::before{content:"• "}
  .headline{font-family:"Quicksand",sans-serif;font-weight:600;font-size:21px;color:var(--teal)}
  .headline-sub{font-family:"Quicksand",sans-serif;font-weight:600;font-size:14px;color:var(--ink);margin-bottom:12px}
  .accent{color:var(--teal);font-weight:600}
  .resources{background:#f1f3f4;padding:8px 10px;margin-top:10px;display:grid;grid-template-columns:1fr 1fr;gap:2px 10px}
  .resources .accent{grid-column:1/3;font-size:9.2px}
  .org-name{display:flex;align-items:center;gap:7px;font-family:"Montserrat",sans-serif;font-weight:700;color:var(--teal);letter-spacing:1px}
  .org-name .mark{display:inline-block;background:var(--teal)}
  .org-name--small{justify-content:center;font-size:20px;margin:18px 0 12px}
  .org-name--small .mark{width:12px;height:12px}
  .org-name--cover{font-size:26px}
  .org-name--cover .mark{width:16px;height:16px}
  .contact{text-align:center}
  .contact p{font-size:9.5px}
  .contact .icon{display:block;margin:8px auto 3px}
  .badge{width:120px;height:42px;margin:10px auto 0;border:1px solid #9db0b8;background:#f3f6f7}
  .pie-wrap{margin-top:10px;position:relative}
  .cover-photo{height:210px;margin:14px -24px 0;background:linear-gradient(135deg,#eef6fa 0%,#c8dfea 35%,#6f9fc4 60%,#dbe9f1 100%)}
  .cover-band{background:var(--teal);margin:0 -24px;padding:10px 24px;color:#fff;display:grid;grid-template-columns:1.3fr 1fr}
  .cover-band p{color:#fff;font-weight:600;font-size:9.5px;grid-column:1/3}
  .cover-band ul{list-style:none}
  .cover-band li{color:#fff;font-size:9.5px}
  .cover-band li::before{content:"• "}
  .cover-text{text-align:center;margin-top:12px}
  .cover-text p{font-size:10px}
  .cover-text .acronym{font-family:"Montserrat",sans-serif;font-weight:700;font-size:13px;color:var(--ink);margin:5px 0 2px}
  .cover-text .full{font-size:11px;color:var(--ink)}
  .registry-callout{background:#f1f3f4;padding:8px 10px;margin:12px 0}
  .website-line{text-align:center;font-size:11px;margin:18px 0}
  .website-line .url{color:var(--teal)}
  .registry-mark{margin-top:14px;height:44px;background:linear-gradient(90deg,#f3f6f8,#d7e3ea);display:flex;flex-direction:column;justify-content:center;padding-left:10px}
  .registry-mark strong{font-family:"Montserrat",sans-serif;color:var(--teal-dark);font-size:13px}
  .registry-mark span{font-size:7.5px;color:var(--ink-soft)}
  .protein-render{height:120px;margin:12px 0;background:radial-gradient(ellipse at 45% 55%,#2b7fd8 0%,#134a8a 35%,#050a14 75%)}
  .symptoms .callout{position:absolute;top:0;left:0;right:0;bottom:38px;margin:0;padding:22px 24px}
  .symptoms p{margin-bottom:5px}
</style>
</head>
<body>

<section class="sheet sheet--outside">
  <article class="panel">
    <div class="callout">
      <h2 class="section-title">What is IBMPFD?</h2>
      <p>Inclusion Body Myopathy associated with Paget's disease of bone &amp; Frontotemporal Dementia is an autosomal dominant mutation in chromosome 9 of the VCP (Valosin Containing Protein) gene. Given the interaction with other genetic diseases, this mutation may also be known as VCP Disease or Disorder.</p>
      <p>Some patients have familial Amyotrophic Lateral Sclerosis (ALS or Lou Gehrig's disease) or Parkinson's which has been shown to have a pathogenic variant in VCP.</p>
    </div>
    <h2 class="section-title">Penetrance by Phenotype</h2>
    <p>The frequency that IBMPFD or VCP Disease manifests itself in one, two, or three primary disorders.</p>
    <ul class="bullets">
      <li>IBM: Inclusion Body Myopathy</li>
      <li>PDB: Paget's Disease of the Bone</li>
      <li>FTD: Frontotemporal Dementia</li>
    </ul>
    <div class="pie-wrap">
      <svg width="325" height="150" viewBox="0 0 325 150" role="img" aria-label="Pie chart of penetrance by phenotype">
        <g transform="translate(162 78) rotate(-90)">
          <circle r="30" fill="none" stroke="#9a9c9e" stroke-width="60" pathLength="100" stroke-dasharray="37 100" stroke-dashoffset="0"/>
          <circle r="30" fill="none" stroke="#f2b705" stroke-width="60" pathLength="100" stroke-dasharray="27 100" stroke-dashoffset="-37"/>
          <circle r="30" fill="none" stroke="#2f5597" stroke-width="60" pathLength="100" stroke-dasharray="1 100" stroke-dashoffset="-64"/>
          <circle r="30" fill="none" stroke="#6aa84f" stroke-width="60" pathLength="100" stroke-dasharray="5 100" stroke-dashoffset="-65"/>
          <circle r="30" fill="none" stroke="#5ba3d9" stroke-width="60" pathLength="100" stroke-dasharray="3 100" stroke-dashoffset="-70"/>
          <circle r="30" fill="none" stroke="#4472c4" stroke-width="60" pathLength="100" stroke-dasharray="10 100" stroke-dashoffset="-73"/>
          <circle r="30" fill="none" stroke="#ed7d31" stroke-width="60" pathLength="100" stroke-dasharray="17 100" stroke-dashoffset="-83"/>
        </g>
        <g font-family="Open Sans, sans-serif" font-size="7" fill="#333">
          <text x="235" y="120">IBM only - 37%</text>
          <text x="20" y="104">IBM &amp; PDB - 27%</text>
          <text x="44" y="30">PDB &amp; FTD - 1%</text>
          <text x="80" y="16">PDB only - 5%</text>
          <text x="128" y="9">FTD only - 3%</text>
          <text x="186" y="9">IBM, PDB, and FTD - 10%</text>
          <text x="228" y="30">IBM &amp; FTD - 16%</text>
        </g>
      </svg>
    </div>
    <div class="panel-foot">www.hopekln.org</div>
  </article>

  <article class="panel">
    <h1 class="headline">Together We Can</h1>
    <p class="headline-sub">Make a Difference</p>
    <h2 class="section-title">PATIENT SUPPORT</h2>
    <p>Hope KLN Disease, Inc. is a 501(c)(3) which was formed to drive efforts to cure diseases related to mutations of the Valosin Containing Protein (VCP) gene. Our main goal is to bring patients and doctors together so we can help one another and drive research towards a cure. We are also trying to bring awareness to the medical community about our rare disease.</p>
    <div class="resources">
      <p class="accent">We offer resources &amp; support to patients, caregivers and doctors. Connect with us.</p>
      <p>• IBMPFD Community page</p>
      <p>• HopeKLN.org<br>• KLNfamilies.org</p>
    </div>
    <div class="org-name org-name--small"><span class="mark"></span>HOPE KLN</div>
    <div class="contact">
      <svg class="icon" width="12" height="12" viewBox="0 0 12 12"><circle cx="6" cy="6" r="6" fill="var(--teal)"/><path d="M3 6.5 6 3.5 9 6.5V9H3Z" fill="#fff"/></svg>
      <p>Hope KLN Disease, Inc.<br>P.O. Box 4120<br>Fairhaven, GA 30000</p>
      <svg class="icon" width="12" height="12" viewBox="0 0 12 12"><circle cx="6" cy="6" r="6" fill="var(--teal)"/><rect x="3" y="4" width="6" height="4.5" fill="#fff"/><path d="M3 4l3 2.5L9 4" stroke="var(--teal)" stroke-width=".7" fill="none"/></svg>
      <p>hopeklndisease@mailbox.org</p>
      <svg class="icon" width="12" height="12" viewBox="0 0 12 12"><circle cx="6" cy="6" r="6" fill="var(--teal)"/><circle cx="6" cy="6" r="3.3" fill="none" stroke="#fff" stroke-width=".8"/><path d="M2.7 6h6.6M6 2.7v6.6" stroke="#fff" stroke-width=".7"/></svg>
      <p>www.hopekln.org</p>
      <div class="badge" role="img" aria-label="Partner membership badge"></div>
    </div>
    <div class="panel-foot"></div>
  </article>

  <article class="panel">
    <div class="org-name org-name--cover"><span class="mark"></span>HOPE KLN</div>
    <div class="cover-photo" role="img" aria-label="Photo of a gloved hand using a pipette beside a laboratory microscope"></div>
    <div class="cover-band">
      <p>Do you have a family history of ADULT ONSET</p>
      <ul><li>Muscle Weakness?</li><li>Dementia?</li><li>Bone Disease?</li></ul>
      <ul><li>ALS?</li><li>Parkinson's?</li><li>IBM?</li></ul>
    </div>
    <div class="cover-text">
      <p>You may consider talking to your doctor about a mutation of the VCP gene called</p>
      <p class="acronym">IBMPFD</p>
      <p class="full">Inclusion Body Myopathy associated with Paget's Disease of Bone &amp; Frontotemporal Dementia.</p>
    </div>
    <div class="panel-foot">www.hopekln.org</div>
  </article>
</section>

<section class="sheet sheet--inside">
  <article class="panel symptoms">
    <div class="callout">
      <h2 class="section-title">SYMPTOMS:</h2>
      <p>IBMPFD, a VCP Disease, is an adult onset disorder that can affect the muscles, bones, and brain, and an affected patient may have any combination of the following conditions:</p>
      <h3 class="sub-title">Inclusion Body Myopathy:</h3>
      <p>The first symptom of IBMPFD is often muscle weakness (myopathy). Typically, patients first notice difficulty raising arms, losing balance or difficulty climbing stairs. As the disorder progresses, weakness develops in the other muscles in the arms, legs &amp; core muscles. Muscle weakness can also affect respiratory and heart (cardiac) muscles. This disorder may first present in an individual's late 30's and over time occurs in approximately 90% of individuals with VCP Disease.</p>
      <h3 class="sub-title">Paget's disease of bone:</h3>
      <p>Bone pain, particularly in the hips and spine, is usually the major symptom of Paget's disease. It most often affects bones of the hips, spine, and skull, and the long bones of the arms and legs. Paget's disease affects half of individuals with VCP Disease and typically first presents in a person's 30's or 40's, which is a much earlier age than those without VCP Disease.</p>
      <h3 class="sub-title">Frontotemporal Dementia:</h3>
      <p>In about one-third of people with VCP Disease, the disorder also affects the brain. FTD typically changes personality, behavior, language &amp; speech. FTD typically presents in the mid-50's.</p>
      <h3 class="sub-title">Amyotrophic Lateral Sclerosis (ALS or Lou Gehrig's disease):</h3>
      <p>ALS occurs in approximately 10% of individuals with VCP Disease. Symptoms include increased muscle tone, weakness, muscle wasting, muscle cramps, difficulty swallowing and speaking.</p>
    </div>
    <div class="panel-foot">www.hopekln.org</div>
  </article>

  <article class="panel">
    <h1 class="headline">Strength through numbers</h1>
    <p class="headline-sub">will help us find a CURE!</p>
    <h2 class="section-title">RESEARCH:</h2>
    <p>The goal of the CaRES registry is to connect as many patients and researchers as possible to help advance treatments and cures for rare diseases.</p>
    <div class="registry-callout">
      <p class="accent">If you have been diagnosed with IBMPFD or VCP Disease, please help us by completing the patient registry through CaRES.</p>
    </div>
    <p class="website-line">Go to our website<br><span class="url">www.hopekln.org</span><br>to access the CaRES Registry.</p>
    <p>The CaRES registry is free for patients to enroll and for researchers to access.</p>
    <p style="margin-top:8px">Please elect for researchers to have access to your registry, as that will greatly assist in the drive for a cure, especially when drug trials are recruiting patients.</p>
    <div class="registry-mark"><strong>CaRES Registry</strong><span>Registry of Rare Conditions</span></div>
    <div class="panel-foot"></div>
  </article>

  <article class="panel">
    <h2 class="section-title">DIAGNOSIS:</h2>
    <p>The only way of diagnosing VCP Disease is through genetic testing. Consult with your doctor about testing for mutations of the VCP gene.</p>
    <p class="accent" style="margin-top:8px">For information about genetic testing, our two medical advisors are available as resources:</p>
    <ul class="bullets">
      <li>Dr. Helen Marlow, Medical Geneticist at Westbrook University<br>hmarlow@westbrook.edu</li>
      <li>Dr. Paul Renner, Neuromuscular Specialist at Eastfield University<br>prenner@eastfield.edu</li>
    </ul>
    <div class="protein-render" role="img" aria-label="Ribbon model of the VCP protein structure on a dark background"></div>
    <h2 class="section-title">TREATMENTS:</h2>
    <p>There is an approved treatment for Paget's disease of bone, so early testing for this disorder is very important.</p>
    <p style="margin-top:6px">There are no known cures or treatments for the Inclusion Body Myopathy or Frontotemporal Dementia. Consult with your doctor about physical therapy, stretching, diet and mobility.</p>
    <div class="panel-foot">www.hopekln.org</div>
  </article>
</section>

</body>
</html>
```